Quarvena Broadband Services TRPL - New Service

This will be an TRPL Mailer promoting internet services

We will be using the 8.5" x 11" TRPL Printing option at

nextdayflyershttps://www.pressloomcards.com/postcard-printing/whole-route-bulk-post

We want to introduce people who have not signed up to our services and let them know what makes us different from out customers.

We offer:

24/7 Technical Support
Flat monthly rates
No data caps
No speed throttling
No long term contracts
No installation fees
Internet Plans start at $39.95/mo

Target Market(s)

Homeowners seeking internet service

Industry/Entity Type

Internet Service Provider

Font styles to use
Other font styles liked:
• RockoFLF

Colors

Designer to choose colors to be used in the design.

Requirements
Must have
• Our logo, website and phone number
• www.quarvena.co
• 555-304-8926
• We want to introduce people to our services with something like "Quarvena Broadband Services are available in your area"
Nice to have
• Our font is called RockoFLF (not a must have if you think something else looks better)
Should not have
• Do not deviate far from our normal color scheme, I would look at our website to get a feel for the colors we use. Usually that blue color
• We do not like cartoonish, I would use stock photos with people using laptops or something
• We have attached an example of a door hanger we have done in the past to show the feel of advertising we like, don't just copy it

```html
<!DOCTYPE html>
<html lang="en">
<head>
<meta charset="utf-8">
<title>Quarvena Broadband Mailer</title>
<link href="https://fonts.googleapis.com/css2?family=Poppins:wght@400;500;600;700&family=Raleway:wght@400;500&display=swap" rel="stylesheet">
<style>
:root{
  --blue:#2586d3;
  --blue-light:#5aaee6;
  --blue-title:#4aa7e6;
  --dark:#2e3036;
  --ink:#26282c;
  --white:#ffffff;
  --stage:#e4e5e7;
}
*{margin:0;padding:0;box-sizing:border-box}
html,body{width:770px;height:1200px;overflow:hidden;background:var(--stage)}
body{position:relative;font-family:'Poppins',sans-serif}
.card{position:absolute;left:27px;width:715px;background:var(--white);overflow:hidden}
.card-front{top:42px;height:550px}
.card-back{top:608px;height:552px}
.abs{position:absolute}
.shapes{position:absolute;left:0;top:0}

.top-bar{left:0;top:0;width:715px;height:56px;background:var(--dark);color:var(--white);
  font-family:'Raleway',sans-serif;font-weight:500;font-size:26px;line-height:56px;text-align:center;letter-spacing:-.2px}
.headline{left:0;top:70px;width:354px;text-align:center;color:var(--white);font-weight:700;font-size:23.5px;line-height:30px;text-transform:uppercase}
.rule{height:2px;background:var(--white);left:21px;width:317px}
.tagline{left:0;top:178px;width:359px;text-align:center;color:var(--white);font-family:'Raleway',sans-serif;font-size:15.5px;line-height:19px;text-transform:uppercase}
.offer-pill{left:15px;top:262px;width:122px;height:23px;border-radius:12px;background:var(--blue-light);color:var(--white);
  font-size:16px;font-weight:500;line-height:24px;text-align:center}
.offer-list{list-style:none;font-size:11px;font-weight:500;color:var(--ink);line-height:18.5px}
.offer-list li{position:relative;padding-left:17px}
.offer-list li::before{content:"";position:absolute;left:2px;top:5px;border-left:7px solid var(--blue-light);border-top:4px solid transparent;border-bottom:4px solid transparent}
.brand{font-weight:500;color:var(--blue);display:flex;align-items:center;gap:8px;line-height:1}
.brand .dot{width:14px;height:14px;border-radius:50%;background:var(--blue)}
.price-text{left:257px;top:411px;width:232px;text-align:center;color:var(--white);font-weight:700;font-size:16px;line-height:21px}
.follow{left:528px;top:424px;font-family:'Raleway',sans-serif;font-size:19px;color:var(--ink)}
.social{width:20px;height:20px;border-radius:50%;background:var(--blue);top:427px}
.site{color:var(--white);font-size:16px;letter-spacing:2.2px;font-weight:500}
.call{left:372px;top:508px;color:var(--white);font-family:'Raleway',sans-serif;font-size:17px;font-weight:500;line-height:24px;white-space:nowrap}
.call .phone-mark{color:var(--blue-light);font-size:13px;margin:0 3px}
.call .avail{color:var(--blue-light);margin-left:8px}

.service{left:0;width:354px;text-align:center}
.service-icon{width:50px;height:50px;border-radius:50%;background:var(--blue);margin:0 auto;display:flex;align-items:center;justify-content:center}
.service-title{color:var(--blue-title);font-family:'Raleway',sans-serif;font-weight:500;font-size:17px;line-height:22px;margin-top:12px}
.service-copy{color:var(--white);font-size:10.4px;line-height:13.6px;margin:12px auto 0;width:322px}
.back-contact{left:22px;top:513px;color:var(--white);font-family:'Raleway',sans-serif;font-weight:500;font-size:17px;line-height:24px;display:flex;align-items:center;gap:8px;white-space:nowrap}
.stamp-box{left:658px;top:435px;width:46px;height:46px;border:1.5px solid var(--ink)}
.address-box{left:523px;top:486px;width:181px;height:58px;border:1.5px solid var(--ink)}
</style>
</head>
<body>

<section class="card card-front">
  <svg class="shapes" width="715" height="550" viewBox="0 0 715 550">
    <defs><linearGradient id="photoTone" x1="0" y1="0" x2="1" y2="1">
      <stop offset="0" stop-color="#d9d2c6"/><stop offset=".5" stop-color="#a98f76"/><stop offset="1" stop-color="#7d6a5c"/></linearGradient></defs>
    <polygon role="img" aria-label="Photo of a smiling couple using a laptop at a kitchen table" points="399,56 715,56 715,374 309,374" fill="url(#photoTone)"/>
    <polygon points="0,56 399,56 349,242 0,242" fill="var(--blue)"/>
    <rect x="0" y="374" width="715" height="4" fill="var(--blue-light)"/>
    <polygon points="257,401 487,401 508,434 487,467 257,467" fill="var(--blue)"/>
    <polygon points="264,407 484,407 501,434 484,461 264,461" fill="none" stroke="var(--white)" stroke-width="1.5" stroke-dasharray="5 3"/>
    <polygon points="350,494 715,494 715,550 0,550 0,528 338,528" fill="var(--dark)"/>
    <polygon points="0,484 258,484 290,513 345,513 338,528 0,528" fill="var(--blue)"/>
    <circle cx="21" cy="506" r="5.5" fill="none" stroke="var(--white)" stroke-width="1.4"/>
    <line x1="15.5" y1="506" x2="26.5" y2="506" stroke="var(--white)" stroke-width="1"/>
  </svg>

  <div class="abs top-bar">YOUR LOCALLY OWNED INTERNET SERVICE PROVIDER</div>
  <h1 class="abs headline">Quarvena will connect<br>your home and business<br>to world</h1>
  <div class="abs rule" style="top:171px"></div>
  <p class="abs tagline">Get your ideas out to the world<br>knowing you are in good hands</p>
  <div class="abs rule" style="top:222px"></div>

  <div class="abs offer-pill">WE OFFER</div>
  <ul class="abs offer-list" style="left:15px;top:299px">
    <li>24/7 Technical Support</li><li>Flat monthly rates</li><li>No data caps</li>
  </ul>
  <ul class="abs offer-list" style="left:168px;top:299px">
    <li>No speed throttling</li><li>No long term contracts</li><li>No installation fees</li>
  </ul>

  <div class="abs brand" style="left:14px;top:412px;font-size:40px"><span class="dot"></span>Quarvena</div>
  <p class="abs price-text">Internet Plans start at<br>$39.95/mo</p>

  <div class="abs follow">follow us</div>
  <span class="abs social" style="left:614px"></span>
  <span class="abs social" style="left:646px"></span>
  <span class="abs social" style="left:680px"></span>

  <div class="abs site" style="left:35px;top:494px">www.quarvena.co</div>
  <div class="abs call">CALL US<span class="phone-mark">&#9742;</span>555-304-8926<span class="avail">AVAILABLE 24/7</span></div>
</section>

<section class="card card-back">
  <svg class="shapes" width="715" height="552" viewBox="0 0 715 552">
    <polygon points="0,0 403,0 349,552 0,552" fill="var(--dark)"/>
    <polygon points="405,0 413,0 362,552 352,552" fill="var(--blue-light)"/>
    <polygon points="0,504 370,504 378,512 378,552 0,552" fill="var(--blue)"/>
  </svg>

  <div class="abs service" style="top:24px">
    <div class="service-icon"><svg width="26" height="24" viewBox="0 0 26 24"><polygon points="13,2 25,13 21,13 21,23 15,23 15,16 11,16 11,23 5,23 5,13 1,13" fill="#fff"/></svg></div>
    <h2 class="service-title">Residential Internet</h2>
    <p class="service-copy">Residential Packages start at $49.95/mo. What you see is what you get with our simple billing promise. We will never add hidden fees or charges and you can expect the same statement each month - all without a contract.</p>
  </div>
  <div class="abs service" style="top:184px">
    <div class="service-icon"><svg width="26" height="22" viewBox="0 0 26 22"><circle cx="8" cy="5" r="3.5" fill="#fff"/><circle cx="15" cy="5" r="3.5" fill="#fff"/><rect x="3" y="10" width="15" height="10" fill="#fff"/><polygon points="18,13 24,10 24,20 18,17" fill="#fff"/></svg></div>
    <h2 class="service-title">Stream HD Video 24/7: Guaranteed</h2>
    <p class="service-copy">We know how frustrating buffering and confusing statements can be. Our vision is a network to handle the High Def content of today's internet and to provide simple billing statements you can count on.</p>
  </div>
  <div class="abs service" style="top:344px">
    <div class="service-icon"><svg width="24" height="28" viewBox="0 0 24 28"><g fill="none" stroke="#fff" stroke-width="1.8"><rect x="2" y="9" width="5" height="12"/><rect x="9.5" y="4" width="5" height="20"/><rect x="17" y="9" width="5" height="12"/></g></svg></div>
    <h2 class="service-title">Quarvena Fiber</h2>
    <p class="service-copy">Residential Packages start at $49.95/mo. What you see is what you get with our simple billing promise. We will never add hidden fees or charges and you can expect the same statement each month - all without a contract.</p>
  </div>

  <div class="abs back-contact"><span>&#9742;</span><span>555-304-8926</span>
    <svg width="16" height="16" viewBox="0 0 16 16" style="margin-left:12px"><circle cx="8" cy="8" r="6" fill="none" stroke="#fff" stroke-width="1.4"/><line x1="2" y1="8" x2="14" y2="8" stroke="#fff"/></svg>
    <span>www.quarvena.co</span></div>

  <div class="abs brand" style="left:434px;top:34px;font-size:42px"><span class="dot"></span>Quarvena</div>
  <div class="abs stamp-box"></div>
  <div class="abs address-box"></div>
</section>

</body>
</html>
```